2 Wine Label Designs

Vintner Bloom has been helping people give customized wine gifts since 1999. From large scale corporate clients, to 1 bottle personalized gifts, we offer a wide range of wines and templates for any occasion. Recently we’ve started to shift our focus to a younger demographic (21 to 35 year old women) and are in the process of updating our website and branding.

One big area we’re working to improve is the customizable wine label/engraving templates we offer on the site (to see our current template library go to www.vintnerbloom-demo.com/shop/wine, select a wine, choose “label” or “engraving” from the dropdown, and click “customize”). You’ll find that a lot of our current templates are outdated or aimed at an older demographic. Over the next few months we want to swap out most of these old templates with fun fresh designs.

We're asking designers to submit 2 customizable wine label templates for this project. One should be wedding themed and the other "Thank You" themed. Please see the attached PDF for more guidelines and creative direction.

Keep in mind, even if you aren't selected as the winner of this project we are going to go through and offer $50 for any label template submitted that we like ($100 if we want both). So there is a good chance you'll be getting some money for your work!

Please read though the attached guidelines PDF carefully (especially the "Must be Customizable" section).

Target Market(s)

21 to 35 year old women

Colors

Designer to choose colors to be used in the design.

Requirements
Must have
• See attached PDF
Nice to have
• See attached PDF
Should not have
• See attached PDF

```html
<!DOCTYPE html>
<html lang="en">
<head>
<meta charset="utf-8">
<title>Wedding Wine Label Template – Vintner Bloom</title>
<link rel="stylesheet" href="https://fonts.googleapis.com/css2?family=Josefin+Sans:wght@300;400&family=Pinyon+Script&family=Great+Vibes&display=swap">
<style>
  :root{
    --backdrop:#8e8987;
    --label-navy:#1d2f45;
    --label-navy-deep:#15212f;
    --gold-light:#f1dcc2;
    --gold:#d9b48f;
    --copper:#c9916e;
    --ampersand:#6f6c76;
    --flower-cream:#f0d3ad;
    --flower-peach:#e3a47d;
    --leaf:#3f6a62;
  }
  *{margin:0;padding:0;box-sizing:border-box}
  html,body{width:1200px;height:1200px;overflow:hidden}
  body{
    background:var(--backdrop);
    display:flex;align-items:center;justify-content:center;
    font-family:"Josefin Sans",sans-serif;
  }
  .wine-label{
    position:relative;
    width:880px;height:1060px;
    background:linear-gradient(160deg,var(--label-navy) 0%,var(--label-navy-deep) 100%);
    overflow:hidden;
    color:var(--gold-light);
    text-align:center;
  }
  .invite-line{
    position:absolute;top:110px;left:0;right:0;
    font-weight:300;font-size:32px;letter-spacing:5px;
    color:var(--gold);
  }
  .wedding-of{
    position:absolute;top:170px;left:0;right:0;
    font-weight:300;font-size:58px;letter-spacing:8px;
    color:var(--gold-light);
  }
  .wedding-of .small{font-size:40px}
  .ampersand{
    position:absolute;top:200px;left:0;right:0;
    font-family:"Great Vibes",cursive;
    font-size:430px;line-height:1;
    color:var(--ampersand);
  }
  .partner{position:absolute;}
  .partner .first-name{
    font-family:"Pinyon Script",cursive;
    font-size:150px;line-height:1;
    background:linear-gradient(90deg,var(--gold-light),var(--copper));
    -webkit-background-clip:text;background-clip:text;color:transparent;
  }
  .partner .middle-name{
    font-weight:300;font-size:28px;letter-spacing:5px;
    color:var(--copper);
  }
  .partner-one{top:340px;left:60px}
  .partner-one .middle-name{text-align:right;margin-top:-18px;padding-right:30px}
  .partner-two{top:360px;right:50px}
  .partner-two .middle-name{text-align:right;margin-top:-10px}
  .event-details{
    position:absolute;top:610px;left:0;right:0;
    font-weight:300;font-size:32px;letter-spacing:5px;line-height:1.35;
    color:var(--gold);
  }
  .floral-band{
    position:absolute;left:0;right:0;bottom:0;height:340px;
    background:
      radial-gradient(ellipse 260px 200px at 40% 65%,var(--flower-cream) 0%,var(--flower-peach) 55%,transparent 80%),
      radial-gradient(ellipse 520px 240px at 55% 75%,var(--leaf) 0%,transparent 75%),
      var(--label-navy-deep);
  }
</style>
</head>
<body>
  <main class="wine-label">
    <p class="invite-line">YOU ARE INVITED TO</p>
    <h1 class="wedding-of"><span class="small">THE</span> WEDDING OF</h1>
    <div class="ampersand" aria-hidden="true">&amp;</div>
    <div class="partner partner-one">
      <div class="first-name">Nora</div>
      <div class="middle-name">JANE</div>
    </div>
    <div class="partner partner-two">
      <div class="first-name">Liam</div>
      <div class="middle-name">GRANT</div>
    </div>
    <p class="event-details">FRIDAY - 12 JULY’18 - 11:00<br>WILLOW COURT - NY</p>
    <div class="floral-band" role="img" aria-label="Illustrated bouquet of cream and peach peonies with green leaves and small white blossoms"></div>
  </main>
</body>
</html>
```